Solar energy proposal for homeowners

I am providing households with solar energy proposals, and I need a high-quality brochure that is packaged cleverly to attract the homeowner's attention. Take a look at the one page solar brochure that I have included to get an idea of text and content.

Target Market(s)

Residential Homeowners

Industry/Entity Type

Solar

Requirements
Must have
• High quality document

```html
<!DOCTYPE html>
<html lang="en">
<head>
<meta charset="utf-8">
<title>Helioria Energy – Solar Flyer</title>
<link href="https://fonts.googleapis.com/css2?family=Barlow:wght@400;500;600;700;800&display=swap" rel="stylesheet">
<style>
  :root {
    --navy: #1e2459;
    --navy-deep: #171c4a;
    --blue: #1ea0dc;
    --sky: #1aa9e0;
    --green: #b2e01f;
    --lime: #a6d81c;
    --teal: #20b2b5;
    --light: #f1f9fc;
    --white: #ffffff;
    --ink: #2b2f45;
    --canvas: #dcdcdc;
  }
  * { box-sizing: border-box; margin: 0; padding: 0; }
  html, body { width: 1200px; height: 2307px; overflow: hidden; }
  body {
    background: var(--canvas);
    font-family: "Barlow", Arial, sans-serif;
    position: relative;
  }
  .flyer {
    position: absolute;
    left: 60px; top: 390px;
    width: 1080px; height: 1527px;
    background: var(--navy);
    overflow: hidden;
    box-shadow: 0 20px 40px rgba(0,0,0,.25);
  }
  /* Hero */
  .hero { position: absolute; left: 0; top: 0; width: 1080px; height: 592px; background: var(--navy); }
  .hero-photo { position: absolute; left: 0; top: 0; width: 1080px; height: 592px; }
  .brand {
    position: absolute; left: 74px; top: 82px;
    display: flex; align-items: center; gap: 18px;
    color: var(--blue); font-size: 62px; font-weight: 400; letter-spacing: 1px; line-height: 1;
  }
  .brand-mark { width: 64px; height: 64px; background: var(--blue); }
  .headline { position: absolute; left: 74px; top: 236px; color: var(--white); line-height: 1; }
  .headline .lead { font-size: 50px; font-weight: 400; display: block; margin-bottom: 12px; }
  .headline .offer {
    font-size: 104px; font-weight: 800; display: block; letter-spacing: -1px;
    background: linear-gradient(90deg, var(--sky) 0%, var(--green) 100%);
    -webkit-background-clip: text; background-clip: text; color: transparent;
    margin-bottom: 6px;
  }
  .headline .line { font-size: 86px; font-weight: 400; display: block; margin-bottom: 4px; letter-spacing: -1px; }

  /* Band */
  .band {
    position: absolute; left: 0; top: 592px; width: 1080px; height: 68px;
    background: linear-gradient(90deg, var(--green) 0%, var(--green) 55%, var(--blue) 100%);
    display: flex; align-items: center; justify-content: center;
    color: var(--navy); font-weight: 700; font-size: 36px; letter-spacing: .2px;
  }

  /* About */
  .about { position: absolute; left: 0; top: 660px; width: 1080px; height: 375px; background: var(--light); }
  .panel-art {
    position: absolute; left: 65px; top: 40px; width: 440px; height: 320px;
    background: linear-gradient(160deg, #4a63c9 0%, #2b3f9e 60%, #c9ced8 100%);
    border-radius: 4px;
  }
  .about-copy { position: absolute; left: 543px; top: 30px; width: 500px; }
  .section-title { color: var(--blue); font-weight: 700; font-size: 32px; line-height: 1; }
  .about-copy p { margin-top: 14px; font-size: 19px; line-height: 25px; color: var(--ink); }
  .about-copy .why { margin-top: 28px; }
  .benefits {
    margin-top: 16px; display: grid; grid-template-columns: 228px 270px;
    list-style: none; font-size: 20px; line-height: 26px; color: var(--navy); font-weight: 500;
  }
  .benefits li::before { content: "• "; }

  /* Services */
  .services { position: absolute; left: 0; top: 1035px; width: 1080px; height: 376px; background: var(--navy); }
  .services-title {
    position: absolute; top: 32px; width: 100%; text-align: center;
    color: var(--green); font-weight: 700; font-size: 34px;
  }
  .service { position: absolute; width: 360px; display: flex; gap: 28px; }
  .service svg { flex: 0 0 88px; width: 88px; height: 88px; }
  .service h3 { color: var(--blue); font-weight: 500; font-size: 20px; line-height: 22px; }
  .service p { color: var(--white); font-weight: 500; font-size: 19px; line-height: 23px; }
  .s1 { left: 93px; top: 105px; }
  .s2 { left: 559px; top: 105px; }
  .s3 { left: 93px; top: 225px; }
  .s4 { left: 559px; top: 225px; }

  /* Footer */
  .footer { position: absolute; left: 0; top: 1411px; width: 1080px; height: 116px; background: var(--teal); }
  .footer-band { position: absolute; left: 0; top: 0; width: 1080px; height: 116px; }
  .address {
    position: absolute; left: 64px; top: 20px; display: flex; gap: 10px;
    color: var(--white); font-size: 21px; line-height: 26px; font-weight: 500;
  }
  .phone {
    position: absolute; left: 380px; top: 30px; width: 340px;
    display: flex; align-items: center; justify-content: center; gap: 8px;
    color: var(--navy); font-weight: 700; font-size: 46px; line-height: 1;
  }
  .web {
    position: absolute; left: 756px; top: 30px;
    color: var(--white); font-size: 21px; line-height: 27px; font-weight: 500;
  }
  .web div { display: flex; align-items: center; gap: 8px; }
</style>
</head>
<body>
<main class="flyer">

  <section class="hero">
    <svg class="hero-photo" viewBox="0 0 1080 592" role="img" aria-label="Photo of a modern house with rooftop solar panels at dusk, lit windows and a green lawn">
      <defs>
        <linearGradient id="photoTone" x1="0" y1="0" x2="0" y2="1">
          <stop offset="0" stop-color="#8ea5c8"/>
          <stop offset="0.45" stop-color="#3a4f86"/>
          <stop offset="0.8" stop-color="#4b6a3a"/>
          <stop offset="1" stop-color="#6fa53a"/>
        </linearGradient>
      </defs>
      <path d="M570 0 C 520 150, 520 330, 530 470 C 520 530, 500 570, 480 592 L1080 592 L1080 0 Z" fill="url(#photoTone)"/>
    </svg>

    <div class="brand"><span class="brand-mark"></span>helioria energy</div>

    <h1 class="headline">
      <span class="lead">SOLAR FOR</span>
      <span class="offer">$0 DOWN.</span>
      <span class="line">NO LIENS.</span>
      <span class="line">NO KIDDING.</span>
    </h1>
  </section>

  <div class="band">POWER YOUR FUTURE WITH HELIORIA ENERGY</div>

  <section class="about">
    <div class="panel-art" role="img" aria-label="Ground-mounted solar panel array on a metal stand"></div>
    <div class="about-copy">
      <h2 class="section-title">ABOUT US</h2>
      <p>At Helioria Energy, our mission is to make solar simple and accessible for everyone. No high-pressure sales—just the information you need to make a smart choice. With our solar rental program, you can lower your monthly energy costs and pay less than your current electricity bill.</p>
      <h2 class="section-title why">WHY CHOOSE US?</h2>
      <ul class="benefits">
        <li>No financing</li>
        <li>No insurance costs</li>
        <li>No liens</li>
        <li>No long-term commitment</li>
        <li>No down payment</li>
        <li>No maintenance costs</li>
      </ul>
    </div>
  </section>

  <section class="services">
    <h2 class="services-title">OUR BEST SERVICE</h2>

    <div class="service s1">
      <svg viewBox="0 0 88 88" aria-hidden="true">
        <path d="M44 4 A40 40 0 0 1 84 44" fill="none" stroke="var(--blue)" stroke-width="4"/>
        <path d="M84 44 A40 40 0 0 1 4 44" fill="none" stroke="var(--green)" stroke-width="4"/>
        <path d="M4 44 A40 40 0 0 1 44 4" fill="none" stroke="var(--blue)" stroke-width="4"/>
        <circle cx="44" cy="40" r="11" fill="none" stroke="#fff" stroke-width="2.5"/>
        <path d="M39 52 h10 M40 57 h8" stroke="#fff" stroke-width="2.5"/>
        <path d="M44 20 v5 M28 28 l4 4 M60 28 l-4 4" stroke="#fff" stroke-width="2.5"/>
      </svg>
      <div><h3>Affordable &amp; Transparent</h3><p>Simple pricing, no hidden fees and a fixed monthly rate lower than typical energy bills.</p></div>
    </div>

    <div class="service s2">
      <svg viewBox="0 0 88 88" aria-hidden="true">
        <path d="M44 4 A40 40 0 0 1 84 44" fill="none" stroke="var(--green)" stroke-width="4"/>
        <path d="M84 44 A40 40 0 0 1 4 44" fill="none" stroke="var(--blue)" stroke-width="4"/>
        <path d="M4 44 A40 40 0 0 1 44 4" fill="none" stroke="var(--blue)" stroke-width="4"/>
        <circle cx="44" cy="44" r="15" fill="none" stroke="#fff" stroke-width="2.5" stroke-dasharray="6 3"/>
        <circle cx="44" cy="44" r="6" fill="none" stroke="#fff" stroke-width="2.5"/>
      </svg>
      <div><h3>Expert Installation</h3><p>Certified professionals handle installation, maintenance, and repairs end to end.</p></div>
    </div>

    <div class="service s3">
      <svg viewBox="0 0 88 88" aria-hidden="true">
        <path d="M44 4 A40 40 0 0 1 84 44" fill="none" stroke="var(--blue)" stroke-width="4"/>
        <path d="M84 44 A40 40 0 0 1 4 44" fill="none" stroke="var(--green)" stroke-width="4"/>
        <path d="M4 44 A40 40 0 0 1 44 4" fill="none" stroke="var(--blue)" stroke-width="4"/>
        <circle cx="44" cy="44" r="17" fill="none" stroke="#fff" stroke-width="2.5"/>
        <circle cx="44" cy="44" r="10" fill="none" stroke="#fff" stroke-width="2.5"/>
        <circle cx="44" cy="44" r="3" fill="#fff"/>
        <path d="M44 44 L60 28" stroke="#fff" stroke-width="2.5"/>
      </svg>
      <div><h3>Local Expertise</h3><p>Florida-based team that understands the needs of Orlando and statewide homeowners.</p></div>
    </div>

    <div class="service s4">
      <svg viewBox="0 0 88 88" aria-hidden="true">
        <path d="M44 4 A40 40 0 0 1 84 44" fill="none" stroke="var(--green)" stroke-width="4"/>
        <path d="M84 44 A40 40 0 0 1 4 44" fill="none" stroke="var(--blue)" stroke-width="4"/>
        <path d="M4 44 A40 40 0 0 1 44 4" fill="none" stroke="var(--blue)" stroke-width="4"/>
        <path d="M44 42 C 44 30, 52 24, 60 24 C 60 34, 54 42, 44 42 Z" fill="none" stroke="#fff" stroke-width="2.5"/>
        <path d="M26 56 h10 l8 -4 h12 M26 62 h24 l12 -8" fill="none" stroke="#fff" stroke-width="2.5"/>
      </svg>
      <div><h3>Eco-Friendly</h3><p>Clean, renewable solar energy that helps reduce your carbon footprint.</p></div>
    </div>
  </section>

  <footer class="footer">
    <svg class="footer-band" viewBox="0 0 1080 116" aria-hidden="true">
      <polygon points="377,0 749,0 703,116 329,116" fill="var(--green)"/>
    </svg>

    <div class="address">
      <svg width="24" height="32" viewBox="0 0 24 32" aria-hidden="true">
        <path d="M12 2 C6 2 2 6.5 2 12 C2 20 12 30 12 30 C12 30 22 20 22 12 C22 6.5 18 2 12 2 Z" fill="none" stroke="var(--navy)" stroke-width="3"/>
        <circle cx="12" cy="12" r="4" fill="var(--navy)"/>
      </svg>
      <div>Helioria Energy, LLC<br>4120 Brightwater Lane<br>Orlando, FL 32801</div>
    </div>

    <div class="phone">
      <svg width="22" height="36" viewBox="0 0 22 36" aria-hidden="true">
        <path d="M16 2 C8 4 3 12 3 18 C3 24 8 32 16 34 L19 28 L13 24 C11 21 11 15 13 12 L19 8 Z" fill="var(--navy)"/>
      </svg>
      555.014.2236
    </div>

    <div class="web">
      <div>
        <svg width="14" height="11" viewBox="0 0 14 11" aria-hidden="true"><rect width="14" height="11" fill="var(--navy)"/><path d="M0 0 L7 6 L14 0" fill="none" stroke="var(--teal)" stroke-width="1.5"/></svg>
        info@helioriaenergy.com
      </div>
      <div>
        <svg width="14" height="14" viewBox="0 0 14 14" aria-hidden="true"><circle cx="7" cy="7" r="6" fill="none" stroke="var(--navy)" stroke-width="1.6"/><path d="M1 7 h12 M7 1 C3 5 3 9 7 13 C11 9 11 5 7 1" fill="none" stroke="var(--navy)" stroke-width="1.2"/></svg>
        www.helioriaenergy.com
      </div>
    </div>
  </footer>

</main>
</body>
</html>
```